Business card for femtech company

Nothing too elaborate but elegant and geared towards the mother and baby market. Prefer full-bleed with logo (attached) rear.

```html
<!DOCTYPE html>
<html lang="en">
<head>
<meta charset="utf-8">
<title>Lunavi Business Card</title>
<link rel="stylesheet" href="https://fonts.googleapis.com/css2?family=Open+Sans:wght@400;600;700&display=swap">
<style>
  :root {
    --teal: #5cc2b9;
    --ink: #1f1f1f;
    --paper: #ffffff;
    --backdrop: #3b3b3b;
  }
  * { box-sizing: border-box; margin: 0; padding: 0; }
  html, body { width: 1200px; height: 689px; overflow: hidden; }
  body {
    background: var(--backdrop);
    font-family: "Open Sans", sans-serif;
    position: relative;
  }
  .card {
    position: absolute;
    top: 194px;
    width: 525px;
    height: 300px;
    background: var(--paper);
    border-radius: 18px;
    overflow: hidden;
  }
  .card--front { left: 45px; }
  .card--back { left: 630px; }

  .wordmark {
    display: flex;
    align-items: center;
    gap: 14px;
    color: var(--teal);
    font-weight: 600;
    letter-spacing: 0.02em;
  }
  .wordmark__dot {
    border-radius: 50%;
    background: var(--teal);
    flex: none;
  }
  .card--front .wordmark {
    position: absolute;
    inset: 0;
    justify-content: center;
    font-size: 76px;
  }
  .card--front .wordmark__dot { width: 70px; height: 70px; }

  .card--back .wordmark {
    position: absolute;
    left: 34px;
    top: 150px;
    font-size: 34px;
    gap: 10px;
  }
  .card--back .wordmark__dot { width: 34px; height: 34px; }

  .divider {
    position: absolute;
    left: 232px;
    top: 40px;
    width: 1.5px;
    height: 175px;
    background: var(--teal);
  }
  .contact {
    position: absolute;
    left: 252px;
    top: 34px;
    color: var(--ink);
    font-size: 12.5px;
    line-height: 1.45;
  }
  .contact__name {
    color: var(--teal);
    font-weight: 700;
    font-size: 20px;
    line-height: 1.15;
  }
  .contact__role { font-size: 12.5px; margin-bottom: 10px; }
  .contact__list { list-style: none; margin-bottom: 10px; }
  .contact__list li { display: flex; align-items: center; gap: 7px; }
  .contact__list svg { width: 11px; height: 11px; fill: var(--teal); flex: none; }
  .contact__address { font-style: normal; }

  .accent-band { position: absolute; left: 0; top: 0; width: 525px; height: 300px; }
</style>
</head>
<body>
  <section class="card card--front" aria-label="Card front">
    <div class="wordmark"><span class="wordmark__dot"></span>lunavi</div>
  </section>

  <section class="card card--back" aria-label="Card back">
    <svg class="accent-band" viewBox="0 0 525 300" aria-hidden="true">
      <path d="M160 300 Q340 255 525 225 L525 300 Z" fill="var(--teal)"/>
    </svg>
    <div class="wordmark"><span class="wordmark__dot"></span>lunavi</div>
    <div class="divider"></div>
    <div class="contact">
      <p class="contact__name">Dana Moreau</p>
      <p class="contact__role">Managing Director</p>
      <ul class="contact__list">
        <li><svg viewBox="0 0 16 16"><path d="M3 1l3 3-2 2c1 2 3 4 5 5l2-2 3 3-2 3C6 15 1 10 1 3z"/></svg>555 014 287</li>
        <li><svg viewBox="0 0 16 16"><path d="M1 3h14v10H1z"/></svg>hello@lunavimail.com</li>
        <li><svg viewBox="0 0 16 16"><circle cx="8" cy="8" r="7"/></svg>www.lunavicare.com</li>
      </ul>
      <address class="contact__address">12 Harbor Lane, Brookdale<br>State, Zip 4821</address>
    </div>
  </section>
</body>
</html>
```